Roofing Contractor business card redesign

I want to redesign my business card with a fresh, eye catching concept

Target Market(s)

Residential Roofing Clients, potential employees, and subcontractors.

Industry/Entity Type

Business

Colors

Designer to choose colors to be used in the design.

Requirements
Nice to have
• I just want something that's more pleasing to the eye. You can use a combination of either / or of my logos.

```html
<!DOCTYPE html>
<html lang="en">
<head>
<meta charset="utf-8">
<title>FairBuild Business Card</title>
<link href="https://fonts.googleapis.com/css2?family=Nunito:wght@400;800&display=swap" rel="stylesheet">
<style>
  :root {
    --backdrop: #5b5b5b;
    --paper: #ffffff;
    --brown: #3d1812;
    --orange: #e8761f;
    --yellow: #f7c41c;
    --yellow-light: #fbd85a;
    --ink: #2b2320;
  }
  * { box-sizing: border-box; margin: 0; padding: 0; }
  html, body { width: 1200px; height: 1200px; overflow: hidden; }
  body {
    background: var(--backdrop);
    font-family: "Nunito", sans-serif;
    position: relative;
  }
  .card {
    position: absolute;
    top: 443px;
    width: 560px;
    height: 313px;
    border-radius: 10px;
    overflow: hidden;
  }
  .card-front { left: 30px; background: var(--paper); }
  .card-back {
    left: 610px;
    background: linear-gradient(135deg, var(--yellow-light) 0%, var(--yellow) 55%, #f2b90d 100%);
  }
  .logo-art {
    position: absolute;
    left: 51px; top: 34px;
    width: 176px; height: 176px;
    border-radius: 50%;
    background: radial-gradient(circle at 50% 40%, #f0a040 0%, #c86a1c 45%, var(--brown) 75%);
  }
  .brand-name {
    position: absolute;
    font-weight: 800;
    color: var(--brown);
    letter-spacing: -0.5px;
    line-height: 1;
  }
  .card-front .brand-name { left: 0; width: 278px; text-align: center; top: 220px; font-size: 40px; }
  .brand-tag {
    position: absolute;
    font-weight: 800;
    color: var(--brown);
    white-space: nowrap;
  }
  .card-front .brand-tag { left: 0; width: 278px; text-align: center; top: 264px; font-size: 14px; }
  .details { position: absolute; left: 264px; top: 30px; }
  .person-name { font-size: 26px; font-weight: 800; color: var(--brown); line-height: 1.2; }
  .person-role { font-size: 15px; color: var(--orange); line-height: 1.3; margin-top: 3px; }
  .divider { width: 25px; height: 2px; background: var(--brown); margin: 12px 0 28px; }
  .contact-list { list-style: none; }
  .contact-list li {
    display: flex; align-items: center; gap: 6px;
    font-size: 17px; color: var(--ink); line-height: 22px;
  }
  .contact-list svg { width: 14px; height: 14px; flex: none; }
  .address { margin-top: 12px; font-size: 17px; color: var(--ink); line-height: 22px; }
  .backdrop-art {
    position: absolute; inset: 0;
    background: linear-gradient(160deg, rgba(255,240,150,0.35) 0%, rgba(230,170,10,0.25) 70%);
  }
  .back-logo {
    position: absolute; left: 0; right: 0; top: 100px;
    display: flex; align-items: center; justify-content: center; gap: 14px;
  }
  .back-logo .brand-name { position: static; font-size: 64px; }
  .back-mark {
    width: 82px; height: 82px; border-radius: 50%;
    background: var(--brown);
  }
  .card-back .brand-tag { left: 0; right: 0; text-align: center; top: 196px; font-size: 21px; }
</style>
</head>
<body>
  <section class="card card-front">
    <div class="logo-art" role="img" aria-label="Illustration of three smiling contractors with tools under a roof, in a round badge"></div>
    <div class="brand-name">FairBuild</div>
    <div class="brand-tag">General Contractors, Inc.</div>
    <div class="details">
      <h1 class="person-name">Mark Delaney</h1>
      <p class="person-role">Keystone Certified Roof Inspector<br>Licensed Property Adjuster</p>
      <div class="divider"></div>
      <ul class="contact-list">
        <li><svg viewBox="0 0 14 14" fill="none" stroke="var(--orange)" stroke-width="1.2"><rect x="3.5" y="0.8" width="7" height="12.4" rx="1.2"/><line x1="6" y1="11" x2="8" y2="11"/></svg>(555) 214-7730</li>
        <li><svg viewBox="0 0 14 14" fill="none" stroke="var(--orange)" stroke-width="1.2"><path d="M3 1.5l2 2.5-1.2 1.5c.8 1.8 2.2 3.2 4 4l1.5-1.2 2.5 2-1.3 2C6 12 2 8 1.2 2.8z"/></svg>(555) 318-6020</li>
        <li><svg viewBox="0 0 14 14" fill="none" stroke="var(--orange)" stroke-width="1.2"><rect x="1" y="3" width="12" height="8.5"/><path d="M1 3l6 5 6-5M1 11.5l4.5-4M13 11.5l-4.5-4"/></svg>mark@fairbuildtx.com</li>
        <li><svg viewBox="0 0 14 14" fill="none" stroke="var(--orange)" stroke-width="1.2"><path d="M1 7l6-5.5L13 7M3 5.5V13h8V5.5M5.8 13V9.5h2.4V13"/></svg>www.fairbuildgc.com</li>
      </ul>
      <p class="address">4821 Cedar Ridge Road Suite, 110<br>Oakvale, TX 75000</p>
    </div>
  </section>

  <section class="card card-back">
    <div class="backdrop-art" role="img" aria-label="Soft faded outline of house rooftops and windows in yellow tones"></div>
    <div class="back-logo">
      <span class="brand-name">FairBuild</span>
      <span class="back-mark"></span>
    </div>
    <div class="brand-tag">General Contractors, Inc.</div>
  </section>
</body>
</html>
```